Create a channel art for human resources youtube channel

We a are human resource company that want to develop a community on youtube. Our channel is call "PVK Studio" and we will produce videos related to human resources topics like: Strategy, Job Description, selection of workers, workers development, Occupational health, Training, etc.

We need a channel art for our youtube channel that communicate to our viewers what is about the channel.

Attach you can see the logo and icon of the channel, also you can see it here: https://www.vidlumo.example/channel/UCqTbWxe7Rk3LmNpaVhyOdZZ

Target Market(s)

The people who is going to see the art - banner for youtube are persons that work on human resources field

Industry/Entity Type

Business

Font styles to use
Sans Serif

Requirements
Must have
• Must to communicate that our channel is about how to do a better and faster human resources to help business improve there productivity , also workers performances and quality work life. Here are some key words to help you inspire:
• Human Resources
• Performance
• Better
• Faster
• Easier
• Business
• Improve
• Health

```html
<!DOCTYPE html>
<html lang="en">
<head>
<meta charset="utf-8">
<title>PVK Studio – Channel Art</title>
<link rel="stylesheet" href="https://fonts.googleapis.com/css2?family=Montserrat:wght@400;600;800;900&display=swap">
<style>
  :root {
    --navy: #073052;
    --sky: #1e7aa3;
    --gold: #f7c31b;
    --silver: #c6c8ca;
    --slate: #56657a;
    --logo-grey: #8d98a3;
    --ring: #c9ced3;
  }
  html, body {
    margin: 0;
    padding: 0;
    overflow: hidden;
    background: var(--navy);
  }
  .banner {
    position: relative;
    width: 1200px;
    height: 328px;
    overflow: hidden;
    background: var(--navy);
    font-family: "Montserrat", sans-serif;
  }
  .backdrop {
    position: absolute;
    inset: 0;
    display: block;
  }
  .brand {
    position: absolute;
    left: 49px;
    top: 49px;
    display: flex;
    align-items: center;
    gap: 10px;
  }
  .brand-dot {
    width: 62px;
    height: 62px;
    border: 1.5px solid var(--ring);
    border-radius: 50%;
    box-sizing: border-box;
  }
  .brand-name {
    color: var(--logo-grey);
    font-weight: 600;
    font-size: 21px;
    letter-spacing: 0.5px;
  }
  .title {
    position: absolute;
    left: 0;
    right: 0;
    top: 82px;
    margin: 0;
    text-align: center;
    line-height: 1;
    transform: translateX(24px);
  }
  .title-main {
    display: block;
    color: var(--silver);
    font-weight: 900;
    font-size: 68px;
    letter-spacing: 2px;
    text-shadow: 3px 4px 4px rgba(0, 0, 0, 0.45);
  }
  .title-sub {
    display: block;
    margin-top: 12px;
    color: var(--slate);
    font-weight: 800;
    font-size: 33px;
    letter-spacing: 3px;
    text-shadow: 2px 3px 3px rgba(0, 0, 0, 0.35);
  }
  .keywords {
    position: absolute;
    left: 0;
    right: 0;
    top: 250px;
    margin: 0;
    text-align: center;
    color: var(--gold);
    font-weight: 400;
    font-size: 19px;
    letter-spacing: 0.4px;
    transform: translateX(-21px);
  }
  .subscribe {
    position: absolute;
    left: 778px;
    top: 305px;
    margin: 0;
    color: var(--gold);
    font-weight: 800;
    font-size: 18px;
    letter-spacing: 0.6px;
  }
</style>
</head>
<body>
  <main class="banner">
    <svg class="backdrop" viewBox="0 0 1280 350" width="1200" height="328" preserveAspectRatio="none" aria-hidden="true">
      <rect width="1280" height="350" fill="var(--navy)"/>
      <polygon points="0,350 1280,0 1280,350" fill="var(--sky)"/>
      <polygon points="0,0 640,0 615,30 0,30" fill="var(--sky)"/>
      <polygon points="670,318 1280,318 1280,350 640,350" fill="var(--navy)"/>
    </svg>

    <div class="brand">
      <span class="brand-dot"></span>
      <span class="brand-name">PVK Studio</span>
    </div>

    <h1 class="title">
      <span class="title-main">PVK</span>
      <span class="title-sub">STUDIO</span>
    </h1>

    <p class="keywords">PERFORMANCE - BETTER - FASTER - EASIER - BUSINESS - IMPROVE - HEALTH</p>

    <p class="subscribe">SUBSCRIBE FOR MORE</p>
  </main>
</body>
</html>
```